Design an Outstanding flyer for my company.

I need a flyer designed for our window tinting company based in Brisbane Queensland Australia. The flyer will be targeting Home tinting. We also do mobile car tinting. Something in regards to this could be incorporated into the flyer as well.
I want it to be 2 sided DL size. Black background.
It really needs to Pop, and be a real attention getter.
It needs to be easy to read.
I have provided a mock up with the info on it from our marketing company. It will need a spellcheck etc to make sure everything is correct.
Everything about it can be changed however you like.
I have also included the company logo.

Lets see what you've got!

Target Market(s)

Home Owners

Industry/Entity Type

Home Improvement

Other font styles liked:
• Duan Penh

Requirements
Must have
• All the information on the mock up. Clear and easy to read.
• Must Stand Out!

```html
<!DOCTYPE html>
<html lang="en">
<head>
<meta charset="utf-8">
<title>Brightline Window Tinting – DL Flyer</title>
<link rel="stylesheet" href="https://fonts.googleapis.com/css2?family=Source+Sans+3:wght@300;400;700;800&display=swap">
<style>
  :root {
    --page-bg: #e6e6e7;
    --flyer-black: #0a0a0a;
    --tint-yellow: #f0de17;
    --tint-yellow-deep: #d6c40a;
    --brand-gold: #e2cd2a;
    --ink-white: #ffffff;
    --ink-black: #0b0b0b;
    --photo-green: #6f8a5a;
    --photo-sky: #c9d3d6;
    --photo-brick: #a0755a;
  }
  * { margin: 0; padding: 0; box-sizing: border-box; }
  html, body {
    width: 1200px; height: 1200px; overflow: hidden;
    background: var(--page-bg);
  }
  body { position: relative; font-family: "Source Sans 3", "Myriad Pro", Arial, sans-serif; }
  .flyer {
    position: absolute; top: 120px; width: 458px; height: 960px;
    background: var(--flyer-black);
    box-shadow: 2px 3px 6px rgba(0,0,0,0.35);
    overflow: hidden;
  }
  .flyer--front { left: 126px; }
  .flyer--back  { left: 619px; }
  .flyer svg { display: block; width: 458px; height: 960px; }
  .headline { font-weight: 800; fill: var(--ink-black); }
  .call-line { font-weight: 700; fill: var(--ink-white); font-size: 28px; }
  .call-accent { fill: var(--brand-gold); }
  .contact-label { font-weight: 300; fill: var(--ink-white); font-size: 44px; }
  .contact-number { font-weight: 800; fill: var(--ink-white); font-size: 46px; }
  .reasons-title { font-weight: 700; fill: var(--tint-yellow); font-size: 36px; text-anchor: middle; }
  .reasons-body { font-weight: 400; fill: var(--ink-white); font-size: 15px; text-anchor: middle; }
  .brand-name { font-weight: 700; fill: var(--brand-gold); font-size: 30px; }
</style>
</head>
<body>

<section class="flyer flyer--front">
  <svg viewBox="0 0 458 960" xmlns="http://www.w3.org/2000/svg">
    <defs>
      <radialGradient id="header-yellow" cx="0.5" cy="0.5" r="0.7">
        <stop offset="0" stop-color="#f7ea3a"/>
        <stop offset="1" stop-color="#d8c608"/>
      </radialGradient>
      <linearGradient id="install-photo" x1="0" y1="0" x2="1" y2="1">
        <stop offset="0" stop-color="#8fa07c"/>
        <stop offset="0.5" stop-color="#5f7a4c"/>
        <stop offset="1" stop-color="#2a2e2a"/>
      </linearGradient>
    </defs>

    <rect class="header-band" x="0" y="0" width="458" height="270" fill="url(#header-yellow)"/>
    <text class="headline" x="22" y="88" font-size="62" textLength="412" lengthAdjust="spacingAndGlyphs">KEEP HEAT OUT</text>
    <text class="headline" x="23" y="134" font-size="46" textLength="410" lengthAdjust="spacingAndGlyphs">BLOCK 99.9% UV RAYS</text>
    <text class="headline" x="23" y="192" font-size="62" textLength="410" lengthAdjust="spacingAndGlyphs">SAVE MONEY</text>
    <text class="headline" x="23" y="242" font-size="48" textLength="410" lengthAdjust="spacingAndGlyphs">INCREASE PRIVACY</text>

    <rect class="install-photo" x="0" y="276" width="458" height="320" fill="url(#install-photo)" role="img" aria-label="Photo of an installer applying tint film to a home window overlooking a garden"/>

    <path class="roofline" d="M0,596 L222,492 L398,548 L398,512 L458,512 L458,960 L0,960 Z" fill="var(--flyer-black)"/>
    <path class="roofline-stroke" d="M0,596 L222,492 L398,548 L398,512 L458,512" fill="none" stroke="var(--brand-gold)" stroke-width="6" stroke-linejoin="round"/>

    <text class="call-line" x="46" y="654" textLength="376" lengthAdjust="spacingAndGlyphs"><tspan class="call-accent">CALL</tspan> BRISBANE’S LEADER IN</text>
    <text class="call-line" x="46" y="684" textLength="374" lengthAdjust="spacingAndGlyphs">HOME WINDOW TINTING <tspan class="call-accent">NOW</tspan></text>

    <text class="contact-label" x="50" y="744" textLength="48" lengthAdjust="spacingAndGlyphs">TEL</text>
    <text class="contact-number" x="125" y="744">:</text>
    <text class="contact-number" x="146" y="744" textLength="273" lengthAdjust="spacingAndGlyphs">07 3000 1234</text>
    <text class="contact-label" x="50" y="792" textLength="60" lengthAdjust="spacingAndGlyphs">SMS</text>
    <text class="contact-number" x="122" y="792">:</text>
    <text class="contact-number" x="142" y="792" textLength="275" lengthAdjust="spacingAndGlyphs">0400 555 128</text>

    <g class="brand">
      <circle cx="58" cy="874" r="26" fill="var(--brand-gold)"/>
      <text class="brand-name" x="100" y="885" textLength="330" lengthAdjust="spacingAndGlyphs">Brightline Window Tinting</text>
    </g>
  </svg>
</section>

<section class="flyer flyer--back">
  <svg viewBox="0 0 458 960" xmlns="http://www.w3.org/2000/svg">
    <defs>
      <linearGradient id="house-photo" x1="0" y1="0" x2="0" y2="1">
        <stop offset="0" stop-color="#b08766"/>
        <stop offset="0.6" stop-color="#8a6c55"/>
        <stop offset="1" stop-color="#3f5a34"/>
      </linearGradient>
      <linearGradient id="door-photo" x1="0" y1="0" x2="1" y2="1">
        <stop offset="0" stop-color="#d4dde0"/>
        <stop offset="0.55" stop-color="#8c9a9e"/>
        <stop offset="1" stop-color="#262a2c"/>
      </linearGradient>
    </defs>

    <rect class="house-photo" x="0" y="0" width="458" height="300" fill="url(#house-photo)" role="img" aria-label="Photo of a brick home with tinted bay windows"/>
    <path class="swoosh-yellow" d="M0,156 Q229,430 458,64 L458,272 Q229,570 0,256 Z" fill="var(--tint-yellow)"/>
    <path class="swoosh-black" d="M0,256 Q229,570 458,272 L458,960 L0,960 Z" fill="var(--flyer-black)"/>

    <circle cx="233" cy="288" r="182" fill="var(--flyer-black)"/>
    <circle class="door-photo" cx="233" cy="288" r="170" fill="url(#door-photo)" role="img" aria-label="Photo of an installer fitting tint film to a glass sliding door"/>

    <text class="reasons-title" x="229" y="532" textLength="286" lengthAdjust="spacingAndGlyphs">20 REASONS WHY</text>
    <text class="reasons-title" x="229" y="572" textLength="398" lengthAdjust="spacingAndGlyphs">HOME WINDOW TINTING</text>
    <text class="reasons-title" x="229" y="612" textLength="338" lengthAdjust="spacingAndGlyphs">IS PERFECT FOR YOU.</text>

    <text class="reasons-body" x="229" y="642" textLength="374" lengthAdjust="spacingAndGlyphs">REDUCE GLARE. REDUCE ENERGY COSTS. CONTROL THE</text>
    <text class="reasons-body" x="229" y="661" textLength="345" lengthAdjust="spacingAndGlyphs">AMOUNT OF LIGHT ENTERING YOUR HOME. REDUCE</text>
    <text class="reasons-body" x="229" y="681" textLength="359" lengthAdjust="spacingAndGlyphs">CARBON FOOTPRINT. MAKE HOME MORE BEAUTIFUL.</text>
    <text class="reasons-body" x="229" y="700" textLength="389" lengthAdjust="spacingAndGlyphs">ELIMINATE HOME HOT SPOTS. PROTECT AGAINST BROKEN</text>
    <text class="reasons-body" x="229" y="719" textLength="378" lengthAdjust="spacingAndGlyphs">GLASS. REGULATE ENERGY. PROTECTS UPHOLSTERY. IM-</text>
    <text class="reasons-body" x="229" y="738" textLength="378" lengthAdjust="spacingAndGlyphs">PROVE EFFECTIVENESS OF ROOF INSULATION. IMPROVE</text>
    <text class="reasons-body" x="229" y="758" textLength="378" lengthAdjust="spacingAndGlyphs">HEALTH. REDUCES INTERIOR FLOOR FADING. ELIMINATE</text>
    <text class="reasons-body" x="229" y="777" textLength="383" lengthAdjust="spacingAndGlyphs">NEED FOR BLINDS. STRENGTHEN YOUR WINDOWS. INSU-</text>
    <text class="reasons-body" x="229" y="797" textLength="218" lengthAdjust="spacingAndGlyphs">LATE IN WINTER. AFFORDABLE.</text>

    <g class="brand">
      <circle cx="58" cy="882" r="26" fill="var(--brand-gold)"/>
      <text class="brand-name" x="100" y="893" textLength="330" lengthAdjust="spacingAndGlyphs">Brightline Window Tinting</text>
    </g>
  </svg>
</section>

</body>
</html>
```